Women's Shelter Website Design

We are working with a Women's Shelter in California. They provide services and shelter for women and mothers throughout California.
Some sites to use for inspiration:
https://harborlightcommons.org
https://qbrtl.org
https://www.kemjy.org
https://plmfarrowby.org
https://www.gvhollow.org (I love the banner, navigation and upper navigation)
https://bellmereroost.org (love the idea of an EXIT NOW button)
Thank you for taking the time to consider designing a website for us. We are web developers based in Stockton, CA, USA. Most of our projects go through the same process. Understanding this process may help you win a project with us. We custom-code all of our websites in-house. We don’t have any requirements as to what tools you use for your design, but we ask that you follow these guidelines.
IMAGES:
If you use any images or icons in the design, we ask that you have a link to the asset so we can purchase the image/icon. Most of the designs we submit do not have the customer’s images on them unless they have some great images. Be creative; show us the feeling you are trying to portray with your image choices. Use any royalty-free site you choose. We subscribe to Adobe and mainly use their images, but we can purchase images outside of Adobe. PLEASE NOTE: we will not submit designs to clients with watermarks on the images.
FONTS:
We ask that you identify the fonts you’re using in the design. This can be done in a message if you want. We typically use Google Fonts and Adobe Fonts.
CONTENT:
We're always open to different content and ideas. We often submit designs with stock images so the client can see our vision. We typically take pictures after the website launch to use their images with our vision. Lorem Ipsum is fine for paragraphs, but we ask that you make the Headers with correct English. We want to be able to show the vision and identify the sections of the website.
INSPIRATION:
We typically add a couple of links in the brief of websites we like to help you get started in your design.
REVISIONS:
We do not often ask for revisions of the designs unless we see something in the design that may not appeal to the client. If there are slight changes that we want to make, we do that in the development process.
FEEDBACK:
We rarely give feedback on designs during the design process. We are working on many website projects and do not have the time to provide feedback. We usually respond if your request is well thought out and asks specific questions, but a note asking “feedback, please” usually goes unanswered.

```html
<!DOCTYPE html>
<html lang="en">
<head>
<meta charset="utf-8">
<title>Marigold Women's Shelter</title>
<link href="https://fonts.googleapis.com/css2?family=Righteous&family=Lato:wght@400;700&family=Marcellus&family=Allura&display=swap" rel="stylesheet">
<style>
:root{
  --purple:#4d2586;
  --purple-deep:#46207c;
  --plum:#a24aa5;
  --orange:#f4574a;
  --green:#3aa63f;
  --mint:#effcef;
  --ink:#2a2a2a;
  --body:#555;
  --line:#d8d8d8;
}
*{margin:0;padding:0;box-sizing:border-box}
html,body{width:1200px;height:3580px;overflow:hidden}
body{position:relative;font-family:'Lato',sans-serif;color:var(--body);background:#fff}
.abs{position:absolute}
.display{font-family:'Righteous',sans-serif;color:var(--ink);text-transform:uppercase;letter-spacing:1px}
.script{font-family:'Allura',cursive;color:var(--green);font-size:40px}
.btn{position:absolute;display:flex;align-items:center;justify-content:center;color:#fff;font-weight:700;font-size:15px;border-radius:24px}

.topbar{top:0;left:0;width:1200px;height:43px;background:var(--purple);color:#fff;font-size:12px;font-weight:700;text-align:center;line-height:43px}

.hero{top:43px;left:0;width:1200px;height:607px;background:#fff;overflow:hidden}
.hero .blob{position:absolute;border-radius:50%;background:#f7f1f8}
.brand{position:absolute;left:110px;top:98px;display:flex;align-items:center;gap:10px;font-family:'Lato',sans-serif;font-weight:700;font-size:30px;color:var(--purple)}
.brand i{display:block;width:28px;height:28px;border-radius:50%;background:var(--plum)}
.nav{position:absolute;top:70px;left:493px;display:flex;gap:26px;font-size:15px;color:#333}
.nav span{padding-bottom:8px}
.nav .on{color:var(--green);border-bottom:2px solid var(--green)}
.lang{position:absolute;left:840px;top:70px;display:flex;align-items:center;gap:6px;font-size:15px;color:#333}
.lang i{display:block;width:30px;height:22px;border-radius:50%;background:linear-gradient(#c23 0 40%,#fff 40% 60%,#c23 60%);position:relative;overflow:hidden}
.lang i:after{content:"";position:absolute;left:0;top:0;width:14px;height:11px;background:#2b3f8e}

.hero-photo-frame{left:610px;top:170px;width:487px;height:525px;background:var(--green);border-radius:4px}
.hero-photo-tab{left:592px;top:152px;width:86px;height:113px;background:#6b6b6b;border-radius:4px}
.hero-photo{left:600px;top:160px;width:488px;height:526px;border-radius:4px;background:linear-gradient(135deg,#b98b72,#d8cbbf 45%,#8f8a86 75%,#35394a)}

.services{top:650px;left:0;width:1200px;height:542px;background:var(--mint)}
.card{position:absolute;top:280px;width:177px;height:170px;background:#fff;border-radius:4px;box-shadow:0 2px 8px rgba(0,0,0,.06);text-align:center}
.card svg{margin-top:28px}
.card p{font-family:'Marcellus',serif;font-size:14px;color:#444;margin-top:14px;letter-spacing:.5px}
.card.active{border-bottom:5px solid var(--green)}

.blog-card{position:absolute;top:1440px;width:471px;height:450px;background:#fff;box-shadow:0 2px 12px rgba(0,0,0,.1);border-radius:4px}
.blog-card .ph{position:absolute;left:6px;top:7px;width:459px;height:233px}
.blog-card h3{position:absolute;left:30px;top:268px;font-family:'Marcellus',serif;font-size:19px;color:#222;letter-spacing:1px;font-weight:400}
.blog-card p{position:absolute;left:32px;top:300px;width:410px;font-size:14px;line-height:24px;color:#666}
.arrow-btn{position:absolute;width:36px;height:36px;border-radius:50%;background:#eee;border:1px solid #ddd;display:flex;align-items:center;justify-content:center}

.mission{top:2000px;left:0;width:1200px;height:528px;background:linear-gradient(180deg,#c4aab6 0%,#b58bb8 45%,#a652ad 75%,#9a3ea8 100%)}
.step{position:absolute;top:2330px;width:200px;text-align:center;color:#fff;font-weight:700;font-size:17px}
.step .c{width:104px;height:104px;margin:0 auto 22px;border-radius:50%;background:var(--orange);display:flex;align-items:center;justify-content:center}

.field{position:absolute;border:1px solid var(--line);background:#fff;font-size:14px;color:#666;padding:17px 16px}
.submit{position:absolute;left:607px;top:2951px;width:288px;height:50px;background:var(--orange);color:#fff;font-weight:700;font-size:14px;display:flex;align-items:center;justify-content:center}

.footer{top:3190px;left:0;width:1200px;height:390px;background:var(--purple-deep)}
.band{left:111px;top:3133px;width:977px;height:100px;border-radius:50px;background:var(--green);color:#fff;font-family:'Righteous',sans-serif;font-size:25px;text-transform:uppercase;letter-spacing:1px;display:flex;align-items:center;justify-content:center}
.col{position:absolute;top:3292px;color:#fff}
.col h4{font-size:20px;font-weight:700;margin-bottom:20px}
.col a{display:block;color:#fff;font-size:14px;line-height:21.5px;text-decoration:none}
.contact li{list-style:none;display:flex;gap:12px;font-size:14px;line-height:21px;margin-bottom:1px}
.contact svg{flex:none;margin-top:4px}
.soc{position:absolute;top:3406px;width:28px;height:28px;border-radius:50%;background:#fff}
</style>
</head>
<body>

<div class="abs topbar">Lorem ipsum dolor sit amet, consectetur adipiscing elit, sed do eiusmod tempor incididunt ut labore et dolore magna aliqua.</div>

<section class="abs hero">
  <div class="blob" style="left:-120px;top:-60px;width:480px;height:480px"></div>
  <div class="blob" style="left:120px;top:240px;width:240px;height:380px;opacity:.7"></div>
  <div class="blob" style="left:640px;top:-180px;width:420px;height:300px;opacity:.6"></div>
  <div class="brand"><i></i>Marigold</div>
  <nav class="nav"><span class="on">Home</span><span>About</span><span>Services</span><span>Blog</span><span>Contact</span></nav>
  <div class="lang"><i></i>EN <svg width="10" height="8" viewBox="0 0 10 8"><path d="M1 2l4 4 4-4" fill="none" stroke="#333" stroke-width="1.4"/></svg></div>
  <div class="btn" style="left:944px;top:22px;width:143px;height:39px;background:var(--orange)">GET A QUOTE</div>
  <div class="abs script" style="left:110px;top:185px">Welcome to</div>
  <h1 class="abs display" style="left:108px;top:236px;font-size:40px;line-height:43px;font-weight:400">Marigold<br>Women's Shelter</h1>
  <p class="abs" style="left:111px;top:329px;width:470px;font-size:14px;line-height:25px">Lorem ipsum dolor sit amet, consectetur adipiscing elit, sed do eiusmod tempor incididunt ut labore et dolore magna aliqua.</p>
  <div class="btn" style="left:111px;top:395px;width:145px;height:38px;background:var(--orange)">GET STARTED</div>
  <svg class="abs" style="left:114px;top:531px" width="80" height="18"><circle cx="9" cy="9" r="7" fill="none" stroke="var(--plum)" stroke-width="1.5"/><circle cx="9" cy="9" r="3.5" fill="var(--plum)"/><circle cx="31" cy="9" r="5.5" fill="none" stroke="#666" stroke-width="1.5"/><circle cx="51" cy="9" r="5.5" fill="none" stroke="#666" stroke-width="1.5"/><circle cx="71" cy="9" r="5.5" fill="none" stroke="#666" stroke-width="1.5"/></svg>
</section>

<div class="abs hero-photo-tab"></div>
<div class="abs hero-photo-frame"></div>
<div class="abs hero-photo" role="img" aria-label="Photo of a smiling counselor seated in an armchair with a notepad"></div>

<section class="abs services">
  <div class="abs script" style="left:0;width:1200px;text-align:center;top:112px">What We Do</div>
  <h2 class="abs display" style="left:0;width:1200px;text-align:center;top:172px;font-size:31px;line-height:35px;font-weight:400">Helping our hurting neighbors<br>rebuild their lives</h2>
  <div class="card" style="left:110px"><svg width="64" height="78" viewBox="0 0 64 78" fill="none" stroke="#8a3b8c" stroke-width="2"><path d="M14 76V58C6 52 4 42 6 32 8 14 24 4 40 6c14 2 22 14 22 28v10l-6 2v12H44v18"/><path d="M34 44l-10-10a6 6 0 0110-6 6 6 0 0110 6z" stroke="var(--orange)"/></svg><p>Emergency Shelters</p></div>
  <div class="card" style="left:310px"><svg width="78" height="78" viewBox="0 0 78 78" fill="none" stroke="#8a3b8c" stroke-width="2"><circle cx="39" cy="39" r="14" stroke="var(--orange)"/><path d="M39 8l5 8 9-3 1 10 10 2-4 9 7 7-8 5 2 10-10 0-3 9-9-5-9 5-3-9-10 0 2-10-8-5 7-7-4-9 10-2 1-10 9 3z"/></svg><p>Residential Program</p></div>
  <div class="card active" style="left:511px"><svg width="78" height="78" viewBox="0 0 78 78" fill="none" stroke="#8a3b8c" stroke-width="2"><rect x="18" y="6" width="48" height="62" rx="4"/><rect x="6" y="22" width="40" height="28" rx="4" stroke="var(--orange)"/><path d="M26 30v12M20 36h12" stroke="var(--orange)"/><circle cx="16" cy="36" r="5"/></svg><p>Children's Resource</p></div>
  <div class="card" style="left:711px"><svg width="90" height="78" viewBox="0 0 90 78" fill="none" stroke="#8a3b8c" stroke-width="2"><path d="M6 76V56c0-10 8-16 18-16h8c10 0 18 6 18 16"/><path d="M14 22C14 12 20 6 28 6s14 6 14 16v8H14z" stroke="var(--orange)"/><circle cx="66" cy="60" r="16"/><path d="M58 52v6a8 8 0 0016 0v-6M66 52v20"/></svg><p>Hunger Relief</p></div>
  <div class="card" style="left:911px"><svg width="78" height="78" viewBox="0 0 78 78" fill="none" stroke="#8a3b8c" stroke-width="2"><path d="M14 26l10-8 10 12-6 6c4 8 10 14 18 18l6-6 12 10-8 10C36 66 12 42 14 26z" stroke="var(--orange)"/><path d="M44 12v8a8 8 0 0016 0v-8M52 8v26"/></svg><p>Hunger Relief</p></div>
</section>

<div class="abs script" style="left:0;width:1200px;text-align:center;top:1260px">Our Blog</div>
<h2 class="abs display" style="left:0;width:1200px;text-align:center;top:1320px;font-size:52px;font-weight:400">Latest Blog</h2>
<p class="abs" style="left:0;width:1200px;text-align:center;top:1389px;font-size:14px">Lorem ipsum dolor sit amet, consectetur adipiscing elit, sed do eiusmod tempor incididunt ut labore et dolore magna aliqua.</p>

<div class="arrow-btn" style="left:39px;top:1670px"><svg width="10" height="12"><path d="M7 1L2 6l5 5" fill="none" stroke="#333" stroke-width="1.5"/></svg></div>
<div class="arrow-btn" style="left:1126px;top:1670px"><svg width="10" height="12"><path d="M3 1l5 5-5 5" fill="none" stroke="#333" stroke-width="1.5"/></svg></div>

<article class="blog-card" style="left:111px">
  <div class="ph" role="img" aria-label="Photo of a smiling woman at a laptop among plants" style="background:linear-gradient(120deg,#5e8a4a,#c9b9a8 45%,#6d5443 70%,#3d5f9a)"></div>
  <h3>LOREM IPSUM DOLOR SIT AMET</h3>
  <p>Lorem ipsum dolor sit amet, consectetur adipiscing elit, sed do eiusmod tempor incididunt ut labore et Lorem ipsum dolor sit incididunt ut labore et dolore magna aliqua.</p>
  <div class="btn" style="left:32px;top:387px;width:144px;height:37px;background:var(--plum)">BUY NOW</div>
</article>
<article class="blog-card" style="left:618px">
  <div class="ph" role="img" aria-label="Photo of a counselor talking with a client in an office" style="background:linear-gradient(100deg,#6c4a3a,#cfc6bf 35%,#e5e0da 60%,#4e6f9a)"></div>
  <h3>LOREM IPSUM DOLOR SIT AMET</h3>
  <p>Lorem ipsum dolor sit amet, consectetur adipiscing elit, sed do eiusmod tempor incididunt ut labore et Lorem ipsum dolor sit incididunt ut labore et dolore magna aliqua.</p>
  <div class="btn" style="left:32px;top:387px;width:144px;height:37px;background:var(--plum)">BUY NOW</div>
</article>

<section class="abs mission" role="img" aria-label="Background photo of a woman on a video call with a counselor, under a purple overlay"></section>
<h2 class="abs display" style="left:0;width:1200px;text-align:center;top:2245px;font-size:36px;color:#fff;font-weight:400">Ways to engage with our mission</h2>
<div class="step" style="left:178px"><div class="c"><svg width="48" height="48" viewBox="0 0 48 48" fill="none" stroke="#fff" stroke-width="2"><rect x="4" y="8" width="40" height="34" rx="3"/><path d="M4 18h40M14 4v8M34 4v8M12 26h4M22 26h4M32 26h4M12 34h4M22 34h4"/></svg></div>Make Schedule</div>
<div class="step" style="left:502px"><div class="c"><svg width="48" height="48" viewBox="0 0 48 48" fill="none" stroke="#fff" stroke-width="2"><circle cx="12" cy="12" r="5"/><circle cx="36" cy="12" r="5"/><circle cx="24" cy="8" r="4"/><path d="M4 40V26c0-4 3-6 8-6s8 2 8 6M28 26c0-4 3-6 8-6s8 2 8 6v14M18 32h12"/></svg></div>Start Discussion</div>
<div class="step" style="left:825px"><div class="c"><svg width="48" height="48" viewBox="0 0 48 48" fill="none" stroke="#fff" stroke-width="2"><rect x="8" y="4" width="28" height="40" rx="3"/><path d="M14 14h16M14 22h16M14 30h10M30 42l12-14 4 4-12 14h-4z"/></svg></div>Enjoy Plan</div>
<svg class="abs" style="left:370px;top:2345px" width="140" height="50" fill="none" stroke="#fff" stroke-width="2.5"><path d="M4 30C40 6 90 2 130 32"/><path d="M116 20l16 14-20 2"/></svg>
<svg class="abs" style="left:695px;top:2345px" width="140" height="50" fill="none" stroke="#fff" stroke-width="2.5"><path d="M4 30C40 6 90 2 130 32"/><path d="M116 20l16 14-20 2"/></svg>

<div class="abs script" style="left:0;width:1200px;text-align:center;top:2600px">Appointment</div>
<h2 class="abs display" style="left:0;width:1200px;text-align:center;top:2672px;font-size:34px;font-weight:400">Book a appointment</h2>
<div class="field" style="left:305px;top:2762px;width:288px;height:50px">First name</div>
<div class="field" style="left:305px;top:2825px;width:288px;height:50px">Last name</div>
<div class="field" style="left:305px;top:2888px;width:288px;height:50px">Email</div>
<div class="field" style="left:305px;top:2951px;width:288px;height:50px">Phone</div>
<div class="field" style="left:607px;top:2762px;width:288px;height:176px">Message</div>
<div class="submit">SUBMIT NOW</div>

<footer class="abs footer"></footer>
<div class="abs band">A strength-based family center.</div>

<div class="abs" style="left:140px;top:3325px;display:flex;align-items:center;gap:10px;color:#fff;font-weight:700;font-size:34px"><i style="display:block;width:30px;height:30px;border-radius:50%;background:#fff"></i>Marigold</div>
<div class="soc" style="left:157px"></div><div class="soc" style="left:192px"></div><div class="soc" style="left:227px"></div><div class="soc" style="left:262px"></div>

<div class="col" style="left:446px"><h4>Quick Links</h4><a>Home</a><a>About</a><a>Services</a><a>Portfolio</a><a>Clients</a><a>Contact</a></div>
<div class="col" style="left:621px"><h4>Information</h4><a>Privacy policy</a><a>Terms &amp; condition</a><a>Support</a><a>Faq</a><a>Team</a></div>
<div class="col contact" style="left:831px"><h4>Contact Us</h4>
<ul>
<li><svg width="12" height="14" viewBox="0 0 12 14"><path d="M6 0a5 5 0 015 5c0 4-5 9-5 9S1 9 1 5a5 5 0 015-5z" fill="var(--orange)"/><circle cx="6" cy="5" r="2" fill="var(--purple-deep)"/></svg><span>123, Lorem ipsum dolor sit<br>consectetur adipiscing elit<br>sed do eius</span></li>
<li><svg width="12" height="12" viewBox="0 0 12 12"><path d="M2 0l3 3-1.5 2a7 7 0 003.5 3.5L9 7l3 3-2 2C5 12 0 7 0 2z" fill="var(--orange)"/></svg><span>+1 888 888 8888</span></li>
<li><svg width="14" height="11" viewBox="0 0 14 11"><rect width="14" height="11" rx="1" fill="var(--orange)"/><path d="M1 1l6 5 6-5" fill="none" stroke="var(--purple-deep)" stroke-width="1.3"/></svg><span>info@companyname.com</span></li>
</ul></div>

<div class="abs" style="left:0;top:3467px;width:120px;height:36px;background:var(--orange);border-radius:0 18px 18px 0;color:#fff;font-weight:700;font-size:14px;display:flex;align-items:center;justify-content:center">EXIT NOW</div>
<div class="abs" style="left:0;width:1200px;text-align:center;top:3516px;color:#fff;font-size:14px">Copyright © 2023. All Rights Reserved</div>

</body>
</html>
```